Stationary Package
Business Card / Letterhead / Envelop
I need double sided standard sized Business Card [3.5" x 2"]
use same look and feel font(s)
Professional
Daniel Whitfield
Marketing Strategist
4518 Harwick Crescent
Mississauga, Ontario, L4T 3K8
danielwhitfield@vellorahaus.com
www.vellorahaus.com
design package for the marketing industry
Logo with tag line
plus the website address
Logo and Tag Line
eps logo
pdf logo version

```html
<!DOCTYPE html>
<html lang="en">
<head>
<meta charset="utf-8">
<title>Daniel Whitfield — Business Cards</title>
<link rel="stylesheet" href="https://fonts.googleapis.com/css2?family=Jost:wght@400;500;700&display=swap">
<style>
  :root {
    --page: #ffffff;
    --blue-light: #3f6fe0;
    --blue-mid: #2a4fd0;
    --blue-deep: #1b2fa8;
    --navy: #0e1f4f;
    --band: #ffffff;
    --brand-blue: #2a53c9;
    --ink-light: #ffffff;
    --grey-light: #6a6a6a;
    --grey-dark: #2f2f2f;
    --card-w: 552px;
    --card-h: 331px;
  }
  * { box-sizing: border-box; margin: 0; padding: 0; }
  html, body {
    width: 1200px; height: 713px; overflow: hidden;
    background: var(--page);
    font-family: "Jost", "Futura", sans-serif;
  }
  .canvas { position: relative; width: 1200px; height: 713px; }
  .card {
    position: absolute; width: var(--card-w); height: var(--card-h);
    overflow: hidden; color: var(--ink-light); text-align: center;
  }
  .card--front { left: 31px; top: 19px;
    background: radial-gradient(ellipse at 50% 45%, var(--blue-light), var(--blue-mid) 55%, var(--blue-deep)); }
  .card--back-blue { left: 619px; top: 19px;
    background: radial-gradient(ellipse at 50% 45%, var(--blue-light), var(--blue-mid) 55%, var(--blue-deep)); }
  .card--back-grey { left: 324px; top: 365px;
    background: radial-gradient(ellipse at 50% 45%, var(--grey-light), #4a4a4a 50%, var(--grey-dark)); }

  .holder-name { position: absolute; top: 24px; width: 100%; font-weight: 700; font-size: 17px; }
  .holder-role { position: absolute; top: 47px; width: 100%; font-size: 12px; }

  .band-stripe { position: absolute; left: 0; top: 122px; width: 100%; height: 9px; background: var(--navy); }
  .band { position: absolute; left: 0; top: 131px; width: 100%; height: 90px; background: var(--band); }
  .band-edge { position: absolute; left: 0; top: 221px; width: 100%; height: 3px; background: var(--blue-deep); }

  .brand { position: absolute; width: 100%; text-align: center; }
  .brand-dot {
    display: block; margin: 0 auto 8px; width: 36px; height: 36px; border-radius: 50%;
    background: var(--ink-light);
  }
  .brand-name { display: block; font-weight: 700; font-size: 25px; letter-spacing: 0.3px; line-height: 1; }
  .brand-tag { display: block; font-size: 12px; margin-top: 3px; }

  .card--front .brand { top: 108px; }
  .card--front .brand-dot { background: var(--brand-blue); border: 3px solid var(--band); }
  .card--front .brand-name { color: var(--brand-blue); font-size: 27px; }
  .card--front .brand-tag { color: var(--brand-blue); }

  .card--back-blue .brand, .card--back-grey .brand { top: 110px; }

  .contact { position: absolute; top: 244px; width: 100%; font-size: 11.5px; line-height: 15.5px; }
  .site { position: absolute; top: 291px; width: 100%; font-size: 11.5px; font-weight: 500; }
</style>
</head>
<body>
<main class="canvas">
  <section class="card card--front" aria-label="Business card front">
    <p class="holder-name">Daniel Whitfield</p>
    <p class="holder-role">Marketing Strategist</p>
    <div class="band-stripe"></div>
    <div class="band"></div>
    <div class="band-edge"></div>
    <div class="brand">
      <span class="brand-dot"></span>
      <span class="brand-name">DANIEL WHITFIELD</span>
      <span class="brand-tag">Vellora Haus</span>
    </div>
    <address class="contact" style="font-style:normal">
      4518 Harwick Crescent Mississauga, Ontario, L4T 3K8<br>
      C : 416 555 0187<br>
      E : danielwhitfield@vellorahaus.com<br>
      www.vellorahaus.com
    </address>
  </section>

  <section class="card card--back-blue" aria-label="Business card back, blue">
    <div class="brand">
      <span class="brand-dot"></span>
      <span class="brand-name">DANIEL WHITFIELD</span>
      <span class="brand-tag">Vellora Haus</span>
    </div>
    <p class="site">www.vellorahaus.com</p>
  </section>

  <section class="card card--back-grey" aria-label="Business card back, grey">
    <div class="brand">
      <span class="brand-dot"></span>
      <span class="brand-name">DANIEL WHITFIELD</span>
      <span class="brand-tag">Vellora Haus</span>
    </div>
    <p class="site">www.vellorahaus.com</p>
  </section>
</main>
</body>
</html>
```